Velmor Crest - Advanced Skincare and undetectable Makeup for Men

We are in need of a professional webpage for our company Velmor Crest. We help every man feel his best by looking his best. Inspired by the myth of Adonis, we offer makeup and skincare products along with education upon their use. Our mission is to celebrate masculinity in all of its forms, regardless of age, race, sexual orientation, or assigned gender at birth.

The webpage would serve as our online store, as a place where our clients can learn about our brand, view our "How-to" video tutorials, and get product information. An online blog will also be hosted in order to keep clients up to date with news, updates, media mentions, etc.

The color schemes that we use are mostly Black and Gold, with Red accents. please keep in mind that this is a men's cosmetics line, and therefore should read powerful, sexy, confident and bold - all with a high end look and feel.

Think along the lines of brands like Dirk Halvan, QBN, Belcuzzi, etc.

our logo is included in the files attached. images and copy will be added in at a later time; hence, general images that fit the feel and filler text is encouraged.

The products to be sold include:
a face cleanser in a pump dispenser bottle (1 size)
a mask in a round jar container (1 size)
a moisturizer in a pump container 1 size)
a concealer in a click pen with a brush applicator (3 shades)
a liquid liner pen (4 shades)
a contouring palette (2 shade options)
a setting spray (single option)

Target Market(s)

Millennial Men

Industry/Entity Type

Beauty

Number of Pages Required

5+ page

Font styles to use
Serif

Colors
ec1f27
000000
faa54b

Requirements
Must have
• ur essential requirements are:
• 1) a stunning and engaging landing page that truly captures the ideals of sexuality, boldness and confidence.
• 2) an interactive and engaging online store that is easy to update / add product / information to.
• 3) Product pages supporting various toggling images of the product, a shade selection option, ingredient information, usage instructions, pricing, and a link to a "how to video" unique to each individual product.
• 4) dedicated space where all of the tutorials can be organized together
• 5) an organized Blog section, that would include a segment for a Q&A section for us to update as the brand grows, ongoing contests (that would be easily hidden if there are no contests running at the moment) as well as general news and updates segment.
• 6) an "about us" page, where our customers are able to learn about our story, inspirations, humanitarian efforts and philosophies in product contents and purity.
• 7) a contact us page, which would include social media links, contact email and telephone number as well as physical address to be updated upon launch.
• 8) discrete privacy policy, terms of use, and return policy links available at the bottom of every page
Nice to have
• 1) A posting forum where clients could post their looks using our products, or maybe a live stream of our Pictoloop account.
• 2) a member sign in page so that we can collect and store customer information for faster check out, keep track of purchases attached to their email address (future loyalty program plans) and maintain an email database for email notifications and the such.

```html
<!DOCTYPE html>
<html lang="en">
<head>
<meta charset="utf-8">
<title>Velmor Crest</title>
<link href="https://fonts.googleapis.com/css2?family=Cinzel:wght@400;600&family=Roboto:ital,wght@0,400;0,500;0,700;1,400&display=swap" rel="stylesheet">
<style>
:root{
  --gold:#e0a21a;
  --gold-soft:#faa54b;
  --red:#ec1f27;
  --black:#000;
  --ink:#0d0d0d;
  --panel:#111;
  --text:#e6e6e6;
  --muted:#9a9a9a;
  --white:#fff;
}
*{box-sizing:border-box;margin:0;padding:0}
html,body{width:1200px;height:3448px;overflow:hidden}
body{background:var(--ink);color:var(--text);font-family:"Roboto",Arial,sans-serif;position:relative}
a{color:inherit;text-decoration:none}
.serif{font-family:"Cinzel",Georgia,serif}

.topbar{height:37px;background:var(--gold);display:flex;justify-content:space-between;align-items:center;padding:0 99px;font-size:12px;color:var(--white)}
.topbar span{margin-right:10px}
.topbar .sep{opacity:.7}

.hero{position:relative;height:618px;overflow:hidden}
.hero-photo{position:absolute;inset:0;background:radial-gradient(circle at 33% 45%,#b97a4c 0,#5a3424 22%,#1e130e 48%,#0a0807 75%),#000}
.hero-glow{position:absolute;left:560px;top:200px;width:420px;height:280px;background:radial-gradient(ellipse,rgba(250,165,75,.35),transparent 65%)}
.nav{position:absolute;top:20px;left:99px;right:99px;display:flex;justify-content:space-between;align-items:center}
.brand{display:flex;align-items:center;gap:10px;font-family:"Cinzel",Georgia,serif;font-size:18px;color:var(--gold);letter-spacing:2px;margin-top:30px}
.brand i{width:14px;height:14px;background:var(--gold);display:block}
.menu{display:flex;gap:30px;font-size:14px;font-weight:500;color:var(--white);margin-top:10px}
.hero-copy{position:absolute;left:644px;top:228px;width:470px}
.hero-copy h1{font-family:"Cinzel",Georgia,serif;font-weight:400;font-size:44px;letter-spacing:4px;color:var(--white)}
.hero-copy p{font-size:16px;line-height:26px;margin:14px 0 20px;color:var(--white)}
.btn-outline{display:inline-block;border:2px solid var(--white);padding:11px 24px;font-size:14px;font-weight:700;color:var(--white)}
.hero-cut{position:absolute;left:0;bottom:0;width:1200px;height:118px}

.about{height:460px;text-align:center;padding-top:78px}
.section-title{font-family:"Cinzel",Georgia,serif;font-weight:400;font-size:34px;letter-spacing:3px;color:var(--white)}
.about p{width:860px;margin:26px auto 0;font-size:13px;line-height:24px;color:var(--text)}
.about p+p{margin-top:14px}
.btn-red{display:inline-block;background:var(--red);color:var(--white);font-size:13px;font-weight:700;padding:11px 28px}
.about .btn-red{margin-top:44px}

.categories{position:relative;height:1195px;background:linear-gradient(180deg,#1b1512,#141110 50%,#0d0c0c);border-top:1px solid #3a2a14}
.row{position:absolute;left:99px;width:1001px;height:294px}
.cat-photo{position:absolute;top:0;width:502px;height:294px}
.cat-panel{position:absolute;top:32px;width:534px;height:230px;background:var(--black);padding:30px 54px}
.cat-panel h2{font-family:"Cinzel",Georgia,serif;font-weight:600;font-size:26px;letter-spacing:3px;color:var(--white)}
.cat-panel p{font-size:12.5px;line-height:22px;margin:14px 0 16px;color:var(--text)}
.cat-panel .btn-red{padding:9px 20px;font-size:12px}
.rule-right{border-right:3px solid var(--gold)}
.rule-left{border-left:3px solid var(--gold)}
.play{position:absolute;left:227px;top:123px}

.blog{height:610px;text-align:center;padding-top:88px}
.cards{position:absolute;top:2498px;left:99px;display:flex;gap:37px}
.card{width:308px;height:377px;background:var(--white);text-align:left;position:relative}
.card-photo{height:200px;border:4px solid var(--white)}
.date{position:absolute;left:4px;top:140px;width:44px;height:56px;color:var(--white);text-align:center;font-family:"Cinzel",Georgia,serif;font-weight:600;font-size:20px;line-height:28px}
.date small{display:block;font-size:11px;line-height:14px}
.date.gold{background:var(--gold)}
.date.red{background:var(--red)}
.card h3{font-size:15px;font-weight:700;color:#222;margin:26px 22px 14px}
.card p{font-size:12px;line-height:20px;color:#888;margin:0 22px}
.meta{position:absolute;left:22px;right:22px;bottom:16px;border-top:1px solid #e5e5e5;padding-top:12px;font-size:11px;color:#777;display:flex;align-items:center;gap:8px}
.meta .dot{color:var(--gold)}
.meta .more{margin-left:auto;color:var(--red);font-style:italic;font-weight:500}

.newsletter{position:absolute;top:2920px;left:0;width:1200px;height:190px;text-align:center}
.newsletter h2{font-family:"Cinzel",Georgia,serif;font-weight:600;font-size:19px;letter-spacing:2px;color:var(--white);margin-top:42px}
.news-line{position:absolute;top:135px;left:0;width:1200px;height:1px;background:var(--red)}
.signup{position:absolute;left:308px;top:107px;width:584px;height:55px;display:flex;border:2px solid var(--red);border-radius:28px;overflow:hidden;background:var(--ink)}
.signup span{flex:1;text-align:left;padding-left:28px;line-height:51px;font-size:13px;font-style:italic;color:var(--text)}
.signup b{width:170px;background:var(--red);color:var(--white);line-height:51px;font-size:16px}

.footer{position:absolute;top:3110px;left:0;width:1200px;height:271px}
.col{position:absolute;top:38px}
.col h4{font-size:15px;font-weight:700;color:var(--white);margin-bottom:18px}
.col li{list-style:none;font-size:12px;line-height:24px;color:var(--text)}
.col li::before{content:"»";color:var(--white);margin-right:18px}
.bottombar{position:absolute;top:3381px;left:0;width:1200px;height:67px;background:var(--gold);text-align:center;line-height:67px;font-size:13px;font-weight:500;color:var(--white)}
</style>
</head>
<body>

<div class="topbar">
  <div><span>Complimentary Shipping &amp; Returns</span><span class="sep">|</span><span>Store Location</span></div>
  <div><span>Log In</span><span class="sep">|</span><span>Register</span><span class="sep">|</span><span>My Cart</span></div>
</div>

<header class="hero">
  <div class="hero-photo" role="img" aria-label="Model blowing golden sparkles from her hand against a dark backdrop"></div>
  <div class="hero-glow"></div>
  <nav class="nav">
    <div class="brand"><i></i>Velmor Crest</div>
    <div class="menu"><a>HOME</a><a>ABOUT</a><a>PRODUCTS</a><a>HOW TO USE</a><a>BLOG</a><a>CONTACT</a>
      <svg width="16" height="16" viewBox="0 0 16 16"><circle cx="6.5" cy="6.5" r="5" fill="none" stroke="#fff" stroke-width="2"/><line x1="10" y1="10" x2="15" y2="15" stroke="#fff" stroke-width="2"/></svg>
    </div>
  </nav>
  <div class="hero-copy">
    <h1>VELMOR CREST</h1>
    <p>At vero eos et accusamus et iusto dignissimos ducimus qui blanditiis praesentium voluptatum deleniti</p>
    <a class="btn-outline">READ MORE &#10148;</a>
  </div>
  <svg class="hero-cut" viewBox="0 0 1200 118" preserveAspectRatio="none">
    <polygon points="0,0 600,100 1200,0 1200,118 0,118" fill="#0d0d0d"/>
    <polygon points="0,0 600,88 1200,0 1200,4 600,114 0,4" fill="#e0a21a"/>
  </svg>
</header>

<section class="about">
  <h2 class="section-title">ABOUT VELMOR CREST</h2>
  <p>At vero eos et accusamus et iusto odio dignissimos ducimus qui blanditiis praesentium voluptatum deleniti atque corrupti quos dolores et quas molestias excepturi sint occaecati cupiditate non provident, similique sunt in culpa animi, id est laborum et dolorum fuga. Et harum quidem rerum facilis est et expedita distinctio. Nam libero tempore, cum soluta nobis est elig cumque nihuo minus id quod maxime...</p>
  <p>Omnis voluptas assumenda est, omnis dolor repellendus. Temporibus autem quibusdam et aut officiis debitis aut rerum necessitatibus saepe eve-niet ut et voluptates repudiandae sint et molestiae non recusandae. Itaque earum rerum hic tenetur a sapiente delectus</p>
  <a class="btn-red">READ MORE &#10148;</a>
</section>

<section class="categories">
  <div class="row" style="top:97px">
    <div class="cat-photo" style="left:0;background:linear-gradient(135deg,#e9d8cc,#b48e78 55%,#6e5447)" role="img" aria-label="Woman applying skin cream in a bathroom"></div>
    <div class="cat-panel rule-right" style="left:467px">
      <h2>SKIN CARE</h2>
      <p>Nemo enim ipsam voluptatem quia voluptas sit aspernatur aut odit aut fugit, sed quia consequuntur magni dolores eos qui ratione voluptatem sequi nesciunt. Neque porro quisquam est, qui dolorem,...</p>
      <a class="btn-red">VIEW ALL &#10148;</a>
    </div>
  </div>
  <div class="row" style="top:444px">
    <div class="cat-photo" style="left:499px;background:linear-gradient(135deg,#d7c1b5,#a0786a 55%,#5a4038)" role="img" aria-label="Hand holding a makeup palette and brush"></div>
    <div class="cat-panel rule-left" style="left:0">
      <h2>MAKEUP</h2>
      <p>Nemo enim ipsam voluptatem quia voluptas sit aspernatur aut odit aut fugit, sed quia consequuntur magni dolores eos qui ratione voluptatem sequi nesciunt. Neque porro quisquam est, qui dolorem,...</p>
      <a class="btn-red">VIEW ALL &#10148;</a>
    </div>
  </div>
  <div class="row" style="top:791px">
    <div class="cat-photo" style="left:0;background:linear-gradient(135deg,#e4d6cc,#a88b7a 55%,#5d463b)" role="img" aria-label="Makeup artist applying eyeshadow to a client, video tutorial">
      <svg class="play" width="48" height="48" viewBox="0 0 48 48"><circle cx="24" cy="24" r="21" fill="rgba(0,0,0,.25)" stroke="#fff" stroke-width="4"/><polygon points="19,14 34,24 19,34" fill="#fff"/></svg>
    </div>
    <div class="cat-panel rule-right" style="left:467px">
      <h2>TUTORIALS</h2>
      <p>Nemo enim ipsam voluptatem quia voluptas sit aspernatur aut odit aut fugit, sed quia consequuntur magni dolores eos qui ratione voluptatem sequi nesciunt. Neque porro quisquam est, qui dolorem,...</p>
      <a class="btn-red">VIEW ALL &#10148;</a>
    </div>
  </div>
</section>

<section class="blog">
  <h2 class="section-title">LATEST BLOG POST</h2>
</section>
<div class="cards">
  <article class="card">
    <div class="card-photo" style="background:linear-gradient(135deg,#2a2020,#8a5a48 50%,#1a1414)" role="img" aria-label="Model applying mascara"></div>
    <div class="date gold">11<small>JUL</small></div>
    <h3>Shrinking From Toil and Pain</h3>
    <p>Dignissimos et ducimus atque qui blanditiis praesentium voluptatum deleniti et quas</p>
    <div class="meta"><span class="dot">&#9679;</span>Arlo Penn <span>|</span> <span class="dot">&#9675;</span>0 Comments<span class="more">More »</span></div>
  </article>
  <article class="card">
    <div class="card-photo" style="background:linear-gradient(135deg,#e6e6e6,#b9a79d 55%,#6b5a52)" role="img" aria-label="Woman at a vanity table with makeup brushes"></div>
    <div class="date red">05<small>JUL</small></div>
    <h3>Expound The Actual Teachings</h3>
    <p>Dignissimos et ducimus atque qui blanditiis praesentium voluptatum deleniti et quas</p>
    <div class="meta"><span class="dot">&#9679;</span>Arlo Penn <span>|</span> <span class="dot">&#9675;</span>0 Comments<span class="more">More »</span></div>
  </article>
  <article class="card">
    <div class="card-photo" style="background:linear-gradient(135deg,#c8d2a8,#b9a286 55%,#6a5a3e)" role="img" aria-label="Friends wearing face masks"></div>
    <div class="date gold">08<small>JUL</small></div>
    <h3>Great Explorer Of The Truth</h3>
    <p>Dignissimos et ducimus atque qui blanditiis praesentium voluptatum deleniti et quas</p>
    <div class="meta"><span class="dot">&#9679;</span>Arlo Penn <span>|</span> <span class="dot">&#9675;</span>0 Comments<span class="more">More »</span></div>
  </article>
</div>

<section class="newsletter">
  <h2>SIGN UP TO OUR NEWSLETTER TO STAY UPDATED</h2>
  <div class="news-line"></div>
  <div class="signup"><span>Your Email Address Here...</span><b>SUBSCRIBE</b></div>
</section>

<footer class="footer">
  <div class="col" style="left:99px"><h4>CUSTOMER CARE</h4><ul><li>Contact Us</li><li>Size Guide</li><li>My Order</li><li>My Account</li><li>Payment</li><li>Authenticity</li></ul></div>
  <div class="col" style="left:384px"><h4>SHIPPING &amp; RETURNS</h4><ul><li>Payment</li><li>Save cards</li><li>Shipping</li><li>Return</li><li>Check Out</li></ul></div>
  <div class="col" style="left:690px"><h4>COMPANY</h4><ul><li>About Us</li><li>Careers</li><li>Reseller</li><li>Blog Post</li></ul></div>
  <div class="col" style="left:904px"><h4>LEGAL AREA</h4><ul><li>Terms and conditions of Sale</li><li>Privacy Policy</li><li>Track your order</li></ul></div>
</footer>

<div class="bottombar">© Copyright 2018 Velmor Crest. All Rights Reserved.</div>

</body>
</html>
```